Business is called "Pelton Ledger". Accounting and tax services.

I need a flyer for my new business "Pelton Ledger". I am an individual accountant working for himself on the Sunshine Coast in Queensland Australia. I would like to see designs that communicate reliability and trust. I believe my point of difference is that I am always available to my clients and I will cap my number of clients to ensure I can service them properly. Accountants in general seem to have a bad reputation for not responding to clients in a timely fashion, whether by email or phone. This is where I intend to differentiate myself. I have included my business card for ideas on colour and for contact information. I have also included some logo's that should go on the flyer. With the QLA logo, the words "Pelton Ledger is a QLA Business" needs to be written either above, below or to the right hand side (as per the business card).

Target Market(s)

Small business owners and individuals requiring taxation and financials

Industry/Entity Type

Public Accounting

Font styles to use
Serif

Requirements
Must have
• Supplied logo's, accounting style pictures etc
Services: Small Business Taxation
Company & Trust Tax Returns
Rental Property Returns
Capital Gains Tax
Individual Tax Returns
BAS and IAS lodgements
Nice to have
• Needs to convey a sense of being reliable and responds to clients quickly.
Should not have
• My name

```html
<!DOCTYPE html>
<html lang="en">
<head>
<meta charset="utf-8">
<title>Pelton Ledger – Flyer</title>
<link rel="stylesheet" href="https://fonts.googleapis.com/css2?family=Raleway:wght@300;400;700;800&family=Roboto+Condensed:wght@400&display=swap">
<style>
  :root {
    --ink: #111111;
    --body-text: #4a4a4a;
    --paper: #ffffff;
    --backdrop: #e9e7e4;
    --photo-warm: #e9c9b8;
    --photo-mid: #d8d2cc;
    --photo-light: #f4f1ee;
    --faint-mark: #ececec;
    --badge-tone: #3a3a3a;
    --badge-soft: #c9c9c9;
  }
  * { box-sizing: border-box; margin: 0; padding: 0; }
  html, body { width: 1184px; height: 1200px; overflow: hidden; }
  body { background: var(--backdrop); font-family: 'Raleway', sans-serif; color: var(--ink); }

  .flyer {
    position: absolute; left: 182px; top: 20px;
    width: 820px; height: 1160px;
    background: var(--paper); overflow: hidden;
    box-shadow: 0 14px 30px rgba(0,0,0,0.22);
  }
  .hero-photo {
    position: absolute; left: 0; top: 0; width: 820px; height: 546px;
    background:
      linear-gradient(180deg, rgba(255,255,255,0) 70%, var(--paper) 100%),
      linear-gradient(90deg, var(--photo-light) 0%, rgba(244,241,238,0.4) 40%, rgba(244,241,238,0) 70%),
      linear-gradient(160deg, var(--photo-warm) 0%, var(--photo-light) 45%, var(--photo-mid) 75%, #cfc6bf 100%);
  }
  .faint-ring {
    position: absolute; left: 403px; top: 715px;
    width: 486px; height: 486px; border-radius: 50%;
    border: 14px solid var(--faint-mark);
  }
  .wordmark {
    position: absolute; left: 50px; top: 328px;
    font-size: 40px; font-weight: 700; letter-spacing: 13px; color: #222;
  }
  .headline {
    position: absolute; left: 55px; top: 400px;
    font-size: 56px; font-weight: 800; line-height: 58px; letter-spacing: -0.5px;
  }
  .intro {
    position: absolute; left: 55px; top: 553px; width: 704px;
    font-size: 21px; font-weight: 300; line-height: 26.5px; letter-spacing: 0.45px;
    color: var(--body-text); text-align: justify;
  }
  .intro p + p { margin-top: 26px; }

  .services-band { position: absolute; left: 55px; top: 786px; width: 708px; height: 46px; }
  .services-band svg { position: absolute; left: 0; top: 0; }
  .services-title {
    position: absolute; left: 33px; top: 7px;
    color: var(--paper); font-size: 27px; font-weight: 700; letter-spacing: 1.5px;
  }
  .service-list { position: absolute; top: 858px; list-style: none; }
  .service-list.left { left: 55px; }
  .service-list.right { left: 448px; }
  .service-list li {
    display: flex; align-items: center; gap: 8px;
    height: 37px; font-size: 23px; font-weight: 400; letter-spacing: 0.3px; color: #222;
  }

  .partner-badge { position: absolute; left: 55px; top: 1026px; width: 164px; height: 72px; background: var(--badge-tone); }
  .partner-caption {
    position: absolute; left: 55px; top: 1102px; width: 170px;
    font-family: 'Roboto Condensed', sans-serif; font-size: 13.5px; color: var(--ink); white-space: nowrap;
  }
  .software-badge { position: absolute; left: 254px; top: 1027px; width: 93px; height: 93px; border-radius: 50%; background: var(--badge-soft); }
  .contact { position: absolute; right: 57px; top: 1022px; text-align: right; }
  .contact .phone { font-size: 60px; font-weight: 800; line-height: 58px; letter-spacing: 0.5px; }
  .contact .web { font-size: 30px; font-weight: 800; line-height: 36px; }
</style>
</head>
<body>
  <main class="flyer">
    <div class="hero-photo" role="img" aria-label="Photo of an accountant at a bright office desk, pointing a pen at a laptop showing a financial report beside a coffee cup"></div>
    <div class="faint-ring" aria-hidden="true"></div>

    <div class="wordmark">PELTON LEDGER</div>
    <h1 class="headline">SUNSHINE COAST IN<br>QUEENSLAND AUSTRALIA</h1>

    <div class="intro">
      <p>I believe my point of difference is that I am always available to my clients &amp; I will cap my number of clients to ensure I can service them properly.</p>
      <p>Accountants in general seem to have a bad reputation for not responding to clients in a timely fashion, whether by email or phone.</p>
      <p>This is where I intend to differentiate myself.</p>
    </div>

    <div class="services-band">
      <svg width="708" height="46" aria-hidden="true">
        <polygon points="0,0 202,0 233,46 0,46" fill="#000"/>
        <line x1="0" y1="45" x2="708" y2="45" stroke="#000" stroke-width="1.5"/>
      </svg>
      <h2 class="services-title">SERVICES</h2>
    </div>

    <ul class="service-list left">
      <li><svg width="30" height="30" viewBox="0 0 30 30" aria-hidden="true"><circle cx="15" cy="15" r="13" fill="none" stroke="#111" stroke-width="2.4"/><path d="M9 15.5l4 4 8-8" fill="none" stroke="#111" stroke-width="2.4"/></svg>Small Business Taxation</li>
      <li><svg width="30" height="30" viewBox="0 0 30 30" aria-hidden="true"><circle cx="15" cy="15" r="13" fill="none" stroke="#111" stroke-width="2.4"/><path d="M9 15.5l4 4 8-8" fill="none" stroke="#111" stroke-width="2.4"/></svg>Company &amp; Trust Tax Returns</li>
      <li><svg width="30" height="30" viewBox="0 0 30 30" aria-hidden="true"><circle cx="15" cy="15" r="13" fill="none" stroke="#111" stroke-width="2.4"/><path d="M9 15.5l4 4 8-8" fill="none" stroke="#111" stroke-width="2.4"/></svg>Rental Property Returns</li>
    </ul>
    <ul class="service-list right">
      <li><svg width="30" height="30" viewBox="0 0 30 30" aria-hidden="true"><circle cx="15" cy="15" r="13" fill="none" stroke="#111" stroke-width="2.4"/><path d="M9 15.5l4 4 8-8" fill="none" stroke="#111" stroke-width="2.4"/></svg>Capital Gains Tax</li>
      <li><svg width="30" height="30" viewBox="0 0 30 30" aria-hidden="true"><circle cx="15" cy="15" r="13" fill="none" stroke="#111" stroke-width="2.4"/><path d="M9 15.5l4 4 8-8" fill="none" stroke="#111" stroke-width="2.4"/></svg>Individual Tax Returns</li>
      <li><svg width="30" height="30" viewBox="0 0 30 30" aria-hidden="true"><circle cx="15" cy="15" r="13" fill="none" stroke="#111" stroke-width="2.4"/><path d="M9 15.5l4 4 8-8" fill="none" stroke="#111" stroke-width="2.4"/></svg>BAS and IAS lodgements</li>
    </ul>

    <div class="partner-badge" aria-hidden="true"></div>
    <p class="partner-caption">Pelton Ledger is a QLA Business</p>
    <div class="software-badge" aria-hidden="true"></div>

    <div class="contact">
      <div class="phone">0412 555 038</div>
      <div class="web">www.peltonledger.com.au</div>
    </div>
  </main>
</body>
</html>
```